Utility Contractor looking for a new website

Water and wastewater utility contractor looking to create a new website that highlights our various services. We are looking for modern web presence that can be updated with current projects and new services as we grow. We have an existing logo that we would like to incorporate into the overall design of the site
Updates

Hi, Thank you for all the design submissions. I have had some time to review and have eliminated the ones I feel are not what I am looking for. Based on the designs that remain, I am looking for a clean (not to many bold colours), modern look that is not to busy (long scrolling page), Thanks, Owen

Target Market(s)

project managers, strata boards, owners, people who make decisions as to who operates their water/wastewater system

Industry/Entity Type

Utility

Font styles to use
Sans Serif

Requirements
Must have
• A min page that describes the company and what we do, A page for each of our services that outlines the service and the benefits of it. the look must be consistent throughout. additionally each service page should have some images related to the service

```html
<!DOCTYPE html>
<html lang="en">
<head>
<meta charset="utf-8">
<title>Clearline Utilities Ltd.</title>
<link rel="stylesheet" href="https://fonts.googleapis.com/css2?family=Lato:ital,wght@0,400;0,700;1,400&family=Crimson+Text:ital@1&display=swap">
<style>
  :root {
    --bg: #ededed;
    --navy: #10294a;
    --ink: #1c3150;
    --muted: #555a60;
    --rule: #d6d6d6;
    --bar: #4a4a4a;
    --accent: #2a6fc4;
    --card-edge: #1fa870;
    --dot: #8a8a8a;
  }
  * { box-sizing: border-box; margin: 0; padding: 0; }
  html, body { width: 1110px; height: 1200px; overflow: hidden; }
  body { background: var(--bg); font-family: "Lato", sans-serif; color: var(--ink); position: relative; }

  .social { position: absolute; top: 4px; left: 890px; display: flex; gap: 14px; }
  .social span { width: 12px; height: 12px; border-radius: 50%; background: var(--accent); display: block; }

  .brand { position: absolute; left: 118px; top: 64px; font-weight: 700; font-size: 22px; line-height: 21px; color: var(--navy); letter-spacing: 0.5px; }

  .nav { position: absolute; top: 124px; left: 0; width: 1110px; font-style: italic; font-size: 16px; color: var(--ink); }
  .nav a { position: absolute; color: inherit; text-decoration: none; }
  .nav .current::before { content: ""; position: absolute; left: -4px; top: -14px; width: 50px; height: 3px; background: var(--bar); }

  .rule { position: absolute; left: 119px; width: 872px; height: 1px; background: var(--rule); }

  .hero { position: absolute; left: 118px; top: 196px; width: 874px; height: 358px;
    background: radial-gradient(ellipse at 50% 55%, #0e1f3a 0%, #3c6a84 30%, #e6e6ef 55%, #5d8aa0 80%, #1d3c63 100%);
    border: 1px solid #6a7d90; }

  .intro { position: absolute; left: 215px; top: 598px; width: 690px; font-family: "Crimson Text", serif; font-style: italic; font-size: 18px; line-height: 24px; color: #555; }
  .intro strong { font-family: "Lato", sans-serif; font-style: normal; font-weight: 400; font-size: 19px; color: var(--navy); }

  .btn { position: absolute; left: 497px; top: 688px; width: 116px; height: 36px; border-radius: 6px; background: var(--navy); color: #fff; font-size: 11px; line-height: 36px; text-align: center; }

  .pager { position: absolute; left: 502px; top: 784px; display: flex; gap: 14px; }
  .pager span { width: 26px; height: 8px; border-radius: 50%; background: var(--dot); display: block; }

  .section-title { position: absolute; left: 118px; top: 868px; font-size: 26px; font-weight: 400; color: var(--navy); }

  .card { position: absolute; top: 925px; width: 280px; }
  .card .photo { width: 280px; height: 200px; border: 1px solid var(--card-edge);
    background: linear-gradient(180deg, #3a72c4 0%, #4f86cf 35%, #d9a640 55%, #8aa0b8 75%, #2e4f8a 100%); }
  .card h3 { font-weight: 400; font-size: 17px; color: var(--navy); margin-top: 14px; }
  .card p { font-size: 11px; line-height: 18px; color: var(--muted); text-align: justify; margin-top: 5px; }
</style>
</head>
<body>
  <div class="social"><span></span><span></span><span></span></div>

  <div class="brand">CLEARLINE<br>UTILITIES LTD.</div>

  <nav class="nav">
    <a class="current" style="left:514px">Home</a>
    <a style="left:591px">Blog</a>
    <a style="left:661px">Portfolio</a>
    <a style="left:761px">Services</a>
    <a style="left:857px">About</a>
    <a style="left:939px">Contact</a>
  </nav>

  <div class="rule" style="top:163px"></div>

  <div class="hero" role="img" aria-label="Close-up of a water droplet rippling a blue water surface"></div>

  <p class="intro">Curabitur cursus est sit amet <strong>dolor pharetra rutrum</strong>. Cum sociis natoque penatibus et magnis dis parturient montes, nascetur ridiculus mus.</p>

  <div class="btn">READ MORE</div>

  <div class="pager"><span></span><span></span><span></span></div>

  <div class="rule" style="top:835px"></div>

  <h2 class="section-title">OUR SERVICES</h2>

  <article class="card" style="left:119px">
    <div class="photo" role="img" aria-label="Colourful water slides against a blue sky"></div>
    <h3>Water service for home</h3>
    <p>Lorem ipsum dolor sit amet, consectetur adipiscing elit. Integer ac neque ligula.</p>
  </article>
  <article class="card" style="left:416px">
    <div class="photo" role="img" aria-label="Colourful water slides against a blue sky"></div>
    <h3>Bottled water delivery</h3>
    <p>Praesent vel turpis sem. Donec feugiat ultrices molestie. Suspendisse aliquet nunc non neque fermentum</p>
  </article>
  <article class="card" style="left:712px">
    <div class="photo" role="img" aria-label="Colourful water slides against a blue sky"></div>
    <h3>Water cooler service</h3>
    <p>Fusce bibendum ante eu urna malesuada eu dapibus magna lobortis. Integer sed nisl at velit elementum.</p>
  </article>
</body>
</html>
```